Corvell's Ride for Autism 2019

we need a flyer for a fundraiser. The fundraiser is hosted by GravelJay Cruisers. It will be on Sunday, April 28th, at 11am. Meet & Greet/registration will be at 11am at Quarrystone Autism Center (5184 Pembrook Fields Drive, Mishawaka, IN 46531) and ending at T.O.K.'s Sports bar and grill. All proceeds will go to the Quarrystone Kinship Circle Foundation. The Foundation helps special needs families with whatever they may need.

Target Market(s)

Motorcyclist

Font styles to use
Sans Serif

Colors

Designer to choose colors to be used in the design.

Requirements
Must have
• Look at Borvanta flyer. We want that kind of style.
Nice to have
• Food, drinks, DJ, 50/50 Raffle, Best Bike award, largest group award, and other amazing prizes.

```html
<!DOCTYPE html>
<html lang="en">
<head>
<meta charset="utf-8">
<title>Corvell's Ride for Autism 2019 – Fundraiser Flyer</title>
<link href="https://fonts.googleapis.com/css2?family=Oswald:wght@600;700&family=Montserrat:wght@700;900&family=Roboto:wght@500;700&display=swap" rel="stylesheet">
<style>
  :root {
    --red: #c0190c;
    --black: #111111;
    --white: #ffffff;
    --sky: #cfe3f1;
    --sky-deep: #9fc2de;
    --road: #8d8f92;
    --foliage: #6f8f55;
  }
  html, body { margin: 0; padding: 0; overflow: hidden; background: #ffffff; }
  .flyer {
    position: relative;
    width: 1200px;
    height: 1200px;
    background: var(--white);
    overflow: hidden;
    font-family: "Montserrat", sans-serif;
  }
  .flyer-art { position: absolute; inset: 0; }
  .club-badge {
    position: absolute;
    left: 80px; top: 320px;
    width: 300px; height: 300px;
    border-radius: 50%;
    background: var(--white);
    border: 10px solid var(--black);
    box-sizing: border-box;
    box-shadow: 0 6px 14px rgba(0,0,0,.25);
    display: flex; align-items: center; justify-content: center;
    text-align: center;
  }
  .club-name {
    font-family: "Montserrat", sans-serif;
    font-weight: 900;
    font-size: 36px;
    line-height: 1.15;
    color: var(--black);
    letter-spacing: 1px;
  }
  .details {
    position: absolute;
    left: 0; right: 0; top: 650px;
    text-align: center;
    padding-left: 120px;
  }
  .headline {
    margin: 0;
    font-family: "Oswald", sans-serif;
    font-weight: 700;
    font-size: 132px;
    line-height: 1;
    color: var(--red);
    letter-spacing: -1px;
  }
  .host-line {
    margin: 6px 0 0;
    font-weight: 900;
    font-size: 50px;
    line-height: 1.1;
    color: var(--black);
  }
  .date-line {
    margin: 22px 0 0;
    font-family: "Roboto", sans-serif;
    font-weight: 700;
    font-size: 34px;
    color: var(--black);
  }
  .date-line .date { color: var(--red); }
  .registration-pill {
    display: inline-block;
    margin-top: 22px;
    padding: 8px 44px;
    border-radius: 40px;
    background: var(--red);
    color: var(--white);
    font-family: "Oswald", sans-serif;
    font-weight: 600;
    font-size: 46px;
    line-height: 1.25;
  }
  .venue-line {
    margin: 14px 0 0;
    font-family: "Roboto", sans-serif;
    font-weight: 500;
    font-size: 21px;
    color: var(--black);
  }
  .footer-rule {
    position: absolute;
    left: 0; right: 0; top: 1090px;
    display: flex; align-items: center;
    padding-left: 40px; padding-right: 40px;
  }
  .footer-rule .rule { flex: 1; height: 4px; background: var(--red); }
  .website-pill {
    margin: 0 14px;
    padding: 12px 56px;
    border-radius: 40px;
    background: var(--black);
    color: var(--red);
    font-family: "Roboto", sans-serif;
    font-weight: 500;
    font-size: 24px;
  }
</style>
</head>
<body>
<main class="flyer">
  <svg class="flyer-art" width="1200" height="1200" viewBox="0 0 1200 1200">
    <defs>
      <linearGradient id="photo-tone" x1="0" y1="0" x2="0" y2="1">
        <stop offset="0" stop-color="#e4eff8"/>
        <stop offset="0.45" stop-color="#b9d3e8"/>
        <stop offset="0.7" stop-color="#7f9a6a"/>
        <stop offset="1" stop-color="#8d8f92"/>
      </linearGradient>
    </defs>
    <path class="hero-photo" role="img" aria-label="Photo of a helmeted rider on a black cruiser motorcycle speeding along a road under a blue sky"
          d="M0,0 H1200 V580 Q700,585 330,400 Q130,300 0,150 Z" fill="url(#photo-tone)"/>
    <path class="hero-swoosh" d="M0,150 Q130,300 330,400 Q700,585 1200,580 L1200,600 Q700,615 320,440 Q120,350 0,260 Z" fill="var(--red)"/>
  </svg>

  <div class="club-badge">
    <span class="club-name">CORVELL<br>UNITED</span>
  </div>

  <section class="details">
    <h1 class="headline">THE FUNDRAISER IS</h1>
    <p class="host-line">HOSTED BY GRAVELJAY CRUISERS</p>
    <p class="date-line">It will be on <span class="date">Sunday, April 28th, at 11am</span></p>
    <div class="registration-pill">MEET &amp; GREET/REGISTRATION WILL BE AT 11AM</div>
    <p class="venue-line">at Quarrystone Autism Center (5184 Pembrook Fields Drive, Mishawaka, IN 46531)</p>
  </section>

  <div class="footer-rule">
    <span class="rule"></span>
    <span class="website-pill">www.corvellunited.com</span>
    <span class="rule"></span>
  </div>
</main>
</body>
</html>
```